Design of a promotional offer flyer required to promote low-cost websites to 1-man band businesses

I want a flyer designed - either a double-sided A5 flyer or even A4 folded into a third double-sided. The flyer is to showcase a new service - low-cost websites for 1-man-band businesses, business startups and tradesmen in England. Look at the copy, find some pix and let me know! Flyer will be printed and used as an image on my website too. Pix could be related to some of the target groups. We need to stress the simple message that websites start from £5 per week and this is an-all-in-one fee.

Target Market(s)

Tradesmen, business start ups and 1-man band businesses that want a website

Industry/Entity Type

Small Business

Contact Information for Business Card

All contact details and name of business to be confirmed shortly

Font styles to use
Serif

Requirements
Must have
• Basic messages from copy for flyer i.e. websites from £5 per week and what each client gets for that price to be included on the business card! Please read copy for the flyer.
Nice to have
• Nice background image or series of small images relevant to the target audience. Again, see list of targets from copy for flyer.
Should not have
• I don't want exact or similar design to my main business Blue Harbour Promotions. The new flyer and business card should be a different and distinct branding to that of Blue Harbour Promotions. Aimed at a more economical style, whilst looking professional, but relevant to the target audiences.

```html
<!DOCTYPE html>
<html lang="en">
<head>
<meta charset="utf-8">
<title>Websites for Tradesmen – Flyer</title>
<link href="https://fonts.googleapis.com/css2?family=Merriweather:wght@700;900&family=Open+Sans:wght@400;600;700&display=swap" rel="stylesheet">
<style>
:root{
  --blue:#1a8fe0;
  --blue-deep:#0b63b8;
  --blue-light:#e7f3fc;
  --navy:#0d3f8a;
  --ink:#1a1a1a;
  --white:#ffffff;
  --backdrop:#d9dadc;
}
*{box-sizing:border-box;margin:0;padding:0}
html,body{width:1200px;height:858px;overflow:hidden}
body{background:var(--backdrop);font-family:"Open Sans",Arial,sans-serif;color:var(--ink);position:relative}
.page{position:absolute;top:39px;width:552px;height:780px;background:var(--white);overflow:hidden;box-shadow:0 4px 14px rgba(0,0,0,.18)}
.page--front{left:36px}
.page--back{left:612px}
.layer{position:absolute;left:0;width:100%}
svg.layer{display:block}

/* front */
.front-photo{top:110px;height:360px;background:radial-gradient(circle at 35% 55%,#f2f4f7 0 18%,#6fb5ea 34%,#1466b8 70%,#0a3f80 100%)}
.front-title{top:26px;text-align:center;font-family:"Merriweather",Georgia,serif;font-weight:900;font-size:29px;line-height:1.15;color:var(--white);padding:0 30px}
.front-headline{top:470px;padding:0 32px;font-family:"Merriweather",Georgia,serif;font-weight:900;font-size:24px;line-height:1.22;color:var(--blue-deep)}
.front-band{top:588px;height:108px;background:var(--blue-deep);color:var(--white);font-size:13.2px;line-height:1.45;padding:16px 30px;text-align:center}
.footer{height:54px;background:var(--blue-deep);color:var(--white);font-weight:700;font-size:17px;letter-spacing:.22em;display:flex;align-items:center;justify-content:center}
.page--front .footer{top:704px}

/* back */
.offer-tab{top:38px;left:26px;width:auto;background:var(--blue-deep);color:var(--white);font-weight:700;font-size:17px;padding:4px 14px;border-radius:0 14px 0 0}
.offer-list{top:76px;left:30px;width:490px;list-style:none;font-size:12.4px;line-height:1.42;counter-reset:item}
.offer-list li{counter-increment:item;padding-left:26px;position:relative}
.offer-list li::before{content:counter(item) ".";position:absolute;left:0}
.bubbles{top:0;height:780px}
.bubble-small-text{top:348px;left:386px;width:112px;text-align:center;color:var(--white);font-size:12px;line-height:1.3}
.bubble-big-text{top:503px;left:110px;width:320px;text-align:center;color:var(--white);font-family:"Merriweather",Georgia,serif;font-weight:900;font-size:17px;line-height:1.35;letter-spacing:.02em}
.contact{top:668px;text-align:center;font-size:12.4px;line-height:1.45}
.page--back .footer{top:726px}
</style>
</head>
<body>

<section class="page page--front">
  <div class="layer front-photo" role="img" aria-label="Hand holding a glowing sphere of web development words over a blue binary-code background"></div>
  <svg class="layer" style="top:0" width="552" height="180" viewBox="0 0 552 180">
    <path d="M0 0H552V96C470 150 360 160 250 130C160 108 80 110 0 142Z" fill="var(--blue)"/>
    <path d="M0 142C80 110 160 108 250 130C360 160 470 150 552 96V112C470 168 360 176 250 148C160 126 80 128 0 160Z" fill="var(--white)"/>
  </svg>
  <h1 class="layer front-title">Want A Website Without<br>It Costing The Earth?</h1>
  <svg class="layer" style="top:400px" width="552" height="80" viewBox="0 0 552 80">
    <path d="M0 50C120 20 260 10 380 40C450 56 510 52 552 30V80H0Z" fill="var(--blue)"/>
    <path d="M0 64C120 34 260 26 380 54C450 70 510 66 552 46V80H0Z" fill="var(--white)"/>
  </svg>
  <h2 class="layer front-headline">Professionally designed websites for tradesmen, business start-ups and 1&#8209;man bands from only £5 per week and NO upfront costs!</h2>
  <p class="layer front-band">Suitable for plumbers, electricians, roofers, builders, painters and decorators, joiners, business start-ups, 1-man bands such as hairdressers, photographers, fitness instructors, window cleaners, beauticians, gardeners, odd job men, wheelie bin cleaners, IFAs or self-employed consultants.</p>
  <div class="layer footer">info@tradesitesdirect.co.uk</div>
</section>

<section class="page page--back">
  <div class="layer offer-tab">Here's what you get:</div>
  <ol class="layer offer-list">
    <li>Professionally-designed 1-page or 5-page website (Home, About Us, Services, Contact Us, News)</li>
    <li>Responsive design that displays properly on mobiles and tablets</li>
    <li>On-going changes and updates</li>
    <li>All text written for you</li>
    <li>Photographs (Royalty-free stock images)</li>
    <li>Professional email addresses e.g. info@tradesitesdirect.co.uk, sales@tradesitesdirect.co.uk and yourname@tradesitesdirect.co.uk. We'll even set up these email addresses on your PC and laptop!</li>
    <li>Links to your social media accounts</li>
    <li>Up to 2 hours' changes each month to content, pix, and adding new pages</li>
    <li>Professional hosting for your website and email</li>
    <li>No upfront cost! Just weekly, monthly or annual invoice - you choose!</li>
  </ol>
  <svg class="layer bubbles" width="552" height="780" viewBox="0 0 552 780" aria-hidden="true">
    <path d="M384 438L404 452L352 482Z" fill="var(--blue)"/>
    <circle cx="442" cy="395" r="78" fill="var(--blue)"/>
    <ellipse cx="270" cy="560" rx="200" ry="100" fill="var(--blue)"/>
  </svg>
  <p class="layer bubble-small-text">For an all in fee from only £5 per week for a 1-page website or £10 per week for a 5-page website.</p>
  <p class="layer bubble-big-text">Promotional Offer: order your new 5-page website before ………… and we'll set up a Friendlink Page for FREE. Normal Cost: £97 plus VAT!</p>
  <p class="layer contact">Visit www.TBC | Call: TBC | Email: TBC<br>For further information or to order. Full terms and conditions at www.TBC.<br>All fees plus VAT.</p>
  <div class="layer footer">info@tradesitesdirect.co.uk</div>
</section>

</body>
</html>
```